Need design for mini jacket of my jazz cd-single

I need a design for my cd package. My song (mp3 file attached) is a jazz interpretation of “Amber Mornings” (a hit song from 1972 by Marla Voss). I’d like the design to be elegant and embody the spirit of my music. I ask that ArtHive artists refrain from using any art that is either copy-written or available for a fee/license only. Using photography, illustrations, drawing, etc. that is 100% license-free is okay.
I will be sending my artwork files to folks at a company called Pine Ridge Disc Works. I want to send them artwork for producing a Mini Jacket of 100 compact discs (http://www.pineridgedisc.example/packaging/wallet.php).
Updates
I am posting an update. I should probably give you designers a little more direction. A landscape design seems obvious and would be totally fitting. But I'd prefer the emphasis to be on my writing and arranging. Therefore, could you try to focus on that? It's still OK to have landscape imagery. Here is a link to some images that I like: https://www.pixelvault.example/illustrations/jazz-piano?sort=mostpopular&mediatype=illustration&phrase=jazz%20piano
I am definitely in favor of you using an illustration of a piano or keyboard because I play piano. If you want to use additional images of other instruments, please make them less prominent than the keyboard image and use only the instruments in my song (acoustic guitar, bass guitar, drums). I make these suggestions because I want the design to be harmonious with my music.
Target Market(s)
My compact discs will be sent to various recording studio engineers who might have clients in need of a composer/arranger/pianist.
Industry/Entity Type
Music Download
Font styles to use
Requirements
Must have
- Included in the design (back panel of 2-panel Mini Jacket), I need the following information:
- (1) the title of the song, which is "Amber Mornings"
- (2) the duration of the song, which is 3:27
- (3) credit given to the songwriters, who are Marla Voss and Lida Marsh
- (4) the copyright symbol, followed by "1972" signifying the year of publication, followed by the name of the publishing company, which is Brightwell Tunes, Inc.
- (5) credit to "Carl Petrov, Jr." as the arranger. Please include the copyright symbol, followed by "2020" signifying the year of publication, followed by my publishing info, which is "Carl Petrov Music, Inc. (RLQ)"
- For the on-disc design, I would like you to incorporate #1, #2, and #5 above.
Nice to have
- Currently, I am working on an arrangement of "Over the Pale Hills" by The Marrowbys. If the design could have a theme that ties together "Amber Mornings" and "Over the Pale Hills," it would be great. Down the road, I might want to modify today's design to accommodate both songs.
Should not have
- Please don't use any artwork or text that requires: (1) someone's permission for use; (2) a fee/license to use. Thank you.

```html
<!DOCTYPE html>
<html lang="en">
<head>
<meta charset="utf-8">
<title>Amber Mornings – Mini Jacket Layout</title>
<link href="https://fonts.googleapis.com/css2?family=Architects+Daughter&family=Bodoni+Moda:wght@400;500&display=swap" rel="stylesheet">
<style>
  :root{
    --backdrop:#7d7769;
    --key-white:#ffffff;
    --key-black:#050505;
    --key-shadow:#a29e95;
    --key-gap:#6f6b62;
    --card-amber:#dca814;
    --tab-yellow:#c6b60c;
    --tab-red:#c4300b;
    --tab-blue:#1179c4;
    --ink:#1d1a14;
    --label-ink:#1f1d1a;
  }
  html,body{margin:0;padding:0;overflow:hidden;}
  body{width:1200px;height:1200px;background:var(--backdrop);position:relative;}
  .panel{position:absolute;width:540px;height:540px;top:30px;}
  .panel--front{left:30px;}
  .panel--back{left:629px;}
  .disc{position:absolute;left:329px;top:630px;width:540px;height:540px;}
  .sheet-label{position:absolute;margin:0;font-family:"Architects Daughter",cursive;font-size:29px;letter-spacing:2px;color:var(--label-ink);line-height:1;}
  .sheet-label--front{left:42px;top:578px;}
  .sheet-label--back{left:653px;top:576px;}
  .sheet-label--disc{left:341px;top:666px;transform:rotate(4deg);}
  svg text{font-family:"Bodoni Moda",serif;fill:var(--ink);}
  .white{fill:var(--key-white);}
  .shadow{fill:var(--key-shadow);}
  .gap{stroke:var(--key-gap);stroke-width:5;}
  .base{fill:var(--key-gap);}
  .black{fill:var(--key-black);}
  .card{fill:var(--card-amber);}
</style>
</head>
<body>

<!-- Front panel -->
<svg class="panel panel--front" viewBox="0 0 870 870" xmlns="http://www.w3.org/2000/svg">
  <defs>
    <linearGradient id="spring" x1="0" y1="0" x2="0" y2="1">
      <stop offset="0" stop-color="#0b0f14"/><stop offset=".8" stop-color="#0b0f14"/><stop offset=".9" stop-color="#2b8a1c"/><stop offset="1" stop-color="#33d11a"/>
    </linearGradient>
    <linearGradient id="summer" x1="0" y1="0" x2="0" y2="1">
      <stop offset="0" stop-color="#2f80c9"/><stop offset=".55" stop-color="#2a5d98"/><stop offset=".7" stop-color="#050505"/><stop offset=".88" stop-color="#050505"/><stop offset="1" stop-color="#5ca033"/>
    </linearGradient>
    <linearGradient id="autumn" x1="0" y1="0" x2="0" y2="1">
      <stop offset="0" stop-color="#050505"/><stop offset=".65" stop-color="#2a140a"/><stop offset=".85" stop-color="#6b3a14"/><stop offset="1" stop-color="#b9961c"/>
    </linearGradient>
    <linearGradient id="winter" x1="0" y1="0" x2="0" y2="1">
      <stop offset="0" stop-color="#050505"/><stop offset=".9" stop-color="#0a0a0a"/><stop offset=".95" stop-color="#cfcfcf"/><stop offset="1" stop-color="#eeeeee"/>
    </linearGradient>
  </defs>
  <rect class="white" width="870" height="870"/>
  <line class="gap" x1="105" y1="560" x2="108" y2="858"/>
  <line class="gap" x1="272" y1="0" x2="272" y2="858"/>
  <line class="gap" x1="435" y1="530" x2="433" y2="858"/>
  <line class="gap" x1="597" y1="555" x2="599" y2="858"/>
  <line class="gap" x1="757" y1="545" x2="760" y2="858"/>
  <rect class="base" x="0" y="858" width="870" height="12"/>

  <polygon class="shadow" points="158,0 187,0 198,580 167,578"/>
  <polygon class="shadow" points="487,0 512,0 498,522 472,527"/>
  <polygon class="shadow" points="648,0 670,0 648,552 632,557"/>
  <polygon class="shadow" points="808,0 845,0 818,548 790,545"/>

  <polygon role="img" aria-label="Spring scene: rain clouds over flowers in green grass" fill="url(#spring)" points="74,0 158,0 167,577 62,557"/>
  <polygon role="img" aria-label="Summer scene: bright sun in a blue sky over a grassy hill" fill="url(#summer)" points="390,0 487,0 472,527 395,542"/>
  <polygon role="img" aria-label="Autumn scene: tree shedding orange leaves at night" fill="url(#autumn)" points="567,0 648,0 632,557 538,559"/>
  <polygon role="img" aria-label="Winter scene: starry night over snow" fill="url(#winter)" points="707,0 808,0 792,545 720,547"/>

  <text x="140" y="840" font-size="58" textLength="92" lengthAdjust="spacingAndGlyphs">Amber</text>
  <text x="294" y="832" font-size="58" textLength="118" lengthAdjust="spacingAndGlyphs">Mornings</text>
</svg>
<p class="sheet-label sheet-label--front">FRONT</p>

<!-- Back panel -->
<svg class="panel panel--back" viewBox="0 0 870 870" xmlns="http://www.w3.org/2000/svg">
  <rect class="white" width="870" height="870"/>
  <line class="gap" x1="105" y1="565" x2="108" y2="858"/>
  <line class="gap" x1="272" y1="0" x2="272" y2="858"/>
  <line class="gap" x1="435" y1="535" x2="435" y2="858"/>
  <line class="gap" x1="597" y1="555" x2="599" y2="858"/>
  <line class="gap" x1="757" y1="542" x2="760" y2="858"/>
  <rect class="base" x="0" y="858" width="870" height="12"/>

  <polygon class="shadow" points="157,0 187,0 198,580 169,569"/>
  <polygon class="shadow" points="487,0 512,0 498,525 472,529"/>
  <polygon class="shadow" points="647,0 670,0 648,550 632,555"/>
  <polygon class="shadow" points="809,0 845,0 815,545 787,542"/>

  <polygon class="black" points="75,0 157,0 169,569 64,557"/>
  <polygon class="black" points="392,0 487,0 472,529 397,542"/>
  <polygon class="black" points="569,0 647,0 632,555 539,557"/>
  <polygon class="black" points="707,0 809,0 787,542 722,544"/>

  <polygon class="shadow" points="637,575 658,578 650,840 627,822"/>
  <polygon class="card" points="279,574 637,566 627,822 282,814"/>
  <g text-anchor="middle">
    <text x="457" y="618" font-size="30" textLength="178" lengthAdjust="spacingAndGlyphs">Amber Mornings 3:27</text>
    <text x="457" y="652" font-size="17" textLength="140" lengthAdjust="spacingAndGlyphs">(Marla Voss, Lida Marsh)</text>
    <text x="457" y="683" font-size="17" textLength="194" lengthAdjust="spacingAndGlyphs">©1972 by Brightwell Tunes, Inc.</text>
    <text x="457" y="756" font-size="22" textLength="228" lengthAdjust="spacingAndGlyphs">Arranged by Carl Petrov, Jr.</text>
    <text x="457" y="791" font-size="17" textLength="242" lengthAdjust="spacingAndGlyphs">©2020 by Carl Petrov Music, Inc. (RLQ)</text>
  </g>
</svg>
<p class="sheet-label sheet-label--back">BACK</p>

<!-- Disc label -->
<p class="sheet-label sheet-label--disc">DISC</p>
<svg class="disc" viewBox="530 1015 870 870" xmlns="http://www.w3.org/2000/svg">
  <defs>
    <clipPath id="disc-face"><circle cx="965" cy="1450" r="435"/></clipPath>
  </defs>
  <g clip-path="url(#disc-face)">
    <rect class="white" x="530" y="1015" width="870" height="870"/>
    <line class="gap" x1="605" y1="1200" x2="598" y2="1885"/>
    <line class="gap" x1="776" y1="1570" x2="780" y2="1885"/>
    <line class="gap" x1="945" y1="1590" x2="947" y2="1885"/>
    <line class="gap" x1="1113" y1="1575" x2="1115" y2="1885"/>
    <line class="gap" x1="1280" y1="1140" x2="1268" y2="1885"/>

    <polygon class="shadow" points="832,1030 857,1030 840,1565 812,1560"/>
    <polygon class="shadow" points="998,1015 1024,1015 1012,1590 982,1585"/>
    <polygon class="shadow" points="1165,1040 1202,1040 1165,1575 1140,1570"/>

    <polygon class="black" points="730,1040 742,1040 748,1575 737,1578"/>
    <polygon fill="var(--tab-yellow)" points="738,1038 832,1030 815,1555 742,1575"/>
    <polygon class="black" points="912,1015 1000,1015 984,1593 885,1593"/>
    <polygon fill="var(--tab-red)" points="915,1018 997,1018 982,1580 887,1580"/>
    <polygon class="black" points="1155,1050 1167,1055 1145,1578 1078,1578 1080,1565 1135,1560"/>
    <polygon fill="var(--tab-blue)" points="1055,1022 1158,1055 1135,1562 1098,1565"/>

    <polygon fill="var(--tab-yellow)" points="760,1627 1146,1622 1146,1690 770,1680"/>
    <polygon fill="var(--tab-red)" points="787,1705 1125,1708 1123,1758 787,1760"/>
    <polygon fill="var(--tab-blue)" points="775,1762 1140,1760 1138,1826 776,1812"/>
    <g text-anchor="middle">
      <text x="958" y="1667" font-size="32" textLength="182" lengthAdjust="spacingAndGlyphs">Amber Mornings 3:27</text>
      <text x="958" y="1745" font-size="28" textLength="264" lengthAdjust="spacingAndGlyphs">Arranged by Carl Petrov, Jr.</text>
      <text x="958" y="1793" font-size="22" textLength="282" lengthAdjust="spacingAndGlyphs">©2020 by Carl Petrov Music, Inc. (RLQ)</text>
    </g>
  </g>
</svg>

</body>
</html>
```